Corporate Business Cards

We need a new design for all of our business cards. They are boring and need some life.

Industry/Entity Type

Business

Requirements
Must have
• Corporate Logo of some type (See attached Pyramid)

Corporate Phrase "steady cashflow"

```html
<!DOCTYPE html>
<html lang="en">
<head>
<meta charset="UTF-8">
<title>Ledgerline Partners — Business Card</title>
<link rel="stylesheet" href="https://fonts.googleapis.com/css2?family=Libre+Bodoni:wght@700&family=Raleway:wght@200&display=swap">
<style>
  :root {
    --backdrop: #e6e6e9;
    --card-navy: #2b2f80;
    --panel-tint: rgba(255, 255, 255, 0.10);
    --ink-white: #ffffff;
    --tagline-tint: #c9cbe8;
    --shadow: rgba(20, 22, 60, 0.25);
  }
  html, body {
    margin: 0;
    padding: 0;
    width: 1200px;
    height: 873px;
    overflow: hidden;
    background: var(--backdrop);
  }
  .stage {
    position: relative;
    width: 1200px;
    height: 873px;
  }
  .business-card {
    position: absolute;
    left: 180px;
    top: 196px;
    width: 840px;
    height: 480px;
    background: var(--card-navy);
    box-shadow: 0 12px 30px var(--shadow);
    overflow: hidden;
  }
  .tint-panel {
    position: absolute;
    right: 0;
    bottom: 0;
    width: 300px;
    height: 150px;
    background: var(--panel-tint);
  }
  .identity {
    position: absolute;
    left: 80px;
    top: 150px;
    display: flex;
    align-items: center;
    gap: 22px;
  }
  .brand-square {
    width: 28px;
    height: 28px;
    background: var(--ink-white);
  }
  .brand-name {
    margin: 0;
    font-family: "Libre Bodoni", "Bodoni Moda", serif;
    font-weight: 700;
    font-size: 46px;
    letter-spacing: 2px;
    line-height: 1;
    color: var(--ink-white);
  }
  .accent-rule {
    position: absolute;
    left: 80px;
    top: 232px;
    width: 680px;
    height: 2px;
    background: var(--ink-white);
  }
  .tagline {
    position: absolute;
    left: 80px;
    top: 256px;
    margin: 0;
    font-family: "Raleway", sans-serif;
    font-weight: 200;
    font-size: 30px;
    letter-spacing: 1px;
    color: var(--tagline-tint);
  }
</style>
</head>
<body>
  <main class="stage">
    <section class="business-card" aria-label="Ledgerline Partners business card">
      <div class="tint-panel"></div>
      <div class="identity">
        <div class="brand-square"></div>
        <h1 class="brand-name">LEDGERLINE PARTNERS</h1>
      </div>
      <div class="accent-rule"></div>
      <p class="tagline">steady cashflow</p>
    </section>
  </main>
</body>
</html>
```